Exclusive Social Networking Platform for future CEOs (no coding required)

We need a creative remake design (from rough mock-ups) for our social networking platform. We are a US-based start-up company called Circle Brightmoor. Our platform allows high-caliber students and young professionals that are part of established networks to reconnect online. It also has an element of Sofahopper.com (host exchange system). In terms of the layout, it can therefore be considered a combination of:
- CareerLoop (CV style profiles)
- FriendWall (messaging, pictures, posts, etc.)
- Sofahopper

UPDATE: We have been asking a few people to try to implement a map of the world (maybe just the outlines) as a backdrop to the platform, but in such a way that it is only faintly noticeable and doesn't become distracting to the platform.

If we really like your designs we may approach you for future designs for a collection of other businesses on a freelance basis (we work out of an incubator).

CONDITIONS: We are only asking for 2 pages as examples (attached PDFs). There may be an opportunity for you to design the rest of the platform as well.
Updates

Thank you very much for your designs so far! There are some very good ones among them. 

Reason: We are still waiting on several designers to provide their edited versions, and we have not yet found the designs we are looking for.

Target Market(s)

Our users are:
1. high-potential global students and young professionals
2. that have been selected to participate in high-end conferences & networks
3. and are typically entrepreneurs, techies, or young corporates
4. they love to travel
5. they are very ambitious about their careers
6. they spend a lot of time meeting people and networking

Industry/Entity Type

It Company

Requirements
Must have
• Base colours (can contain any combination of the following—you can also exclude blue if you like):
- Dark grey (almost black)
- lighter greys
- white
- blue

In terms of the design, please base it on the functional layouts we have provided (attached files). Feel free to redesign as you wish (both in colour and structure), as long as it keeps the functionality outlined by the rough sketches.
- please redesign the icons at the top (News Feed, Events, BedSwap, Expeditions) to a very simple and attractive format

NOTE: Please provide one design for each of the 2 PDF files ('RoamHub' and 'Profile') to show us how you creatively visualise the platform ('RoamHub' is the most up-to-date version considering the icons on the top and the general layout). Please also consider the attached logo to get a feeling of our brand.
Nice to have
• We would be happy to see a creative infusion of the colourful colours of our logo (see attached file). With this, it would be important that it would be kept to a minimum (as otherwise it will be distracting), so a good place to include it may be in the icons that direct people around the site, or in other parts that are more creative—up to you!

```html
<!DOCTYPE html>
<html lang="en">
<head>
<meta charset="utf-8">
<title>Circle Brightmoor – Profile</title>
<link href="https://fonts.googleapis.com/css2?family=Arimo:wght@400;700&family=Open+Sans:wght@400;600&display=swap" rel="stylesheet">
<style>
:root{
  --page:#ececec;
  --map:#e2e2e2;
  --bar:#dcdcdc;
  --bar-line:#b9b9b9;
  --ink:#1c1c1c;
  --text:#444;
  --muted:#666;
  --panel:#ffffff;
  --panel-line:#c9c9c9;
  --panel-head:#d9d9d9;
  --dark:#666666;
  --darker:#2b2b2b;
  --footer:#5a5a5a;
  --link:#3b64c8;
  --day:#4d74c9;
  --online:#1fb81f;
  --badge:#222;
}
*{box-sizing:border-box;margin:0;padding:0}
html,body{width:1200px;height:724px;overflow:hidden}
body{background:var(--page);font-family:Arimo,Arial,sans-serif;color:var(--text);position:relative}
.abs{position:absolute}
.world-map{position:absolute;left:12px;top:80px;width:1176px;height:580px;background:radial-gradient(ellipse at 30% 45%,var(--map) 0%,rgba(226,226,226,0) 60%),radial-gradient(ellipse at 75% 40%,var(--map) 0%,rgba(226,226,226,0) 55%)}
/* top bar */
.topbar{position:absolute;left:0;top:5px;width:1200px;height:27px;background:linear-gradient(#f2f2f2,var(--bar));border-bottom:1px solid var(--bar-line)}
.brand{position:absolute;left:258px;top:12px;font-size:13px;letter-spacing:.2px;color:var(--ink);display:flex;align-items:center;gap:5px}
.brand-dot{width:10px;height:10px;border-radius:50%;background:#8a8a8a}
.search{position:absolute;left:414px;top:8px;width:261px;height:19px;background:#fff;border:1px solid #c5c5c5;font-size:9px;color:#999;padding:4px 0 0 22px}
.search svg{position:absolute;left:7px;top:4px}
.top-icons svg{position:absolute}
.badge{position:absolute;background:var(--badge);color:#fff;font-size:8px;line-height:10px;padding:0 2px;min-width:9px;text-align:center}
.tooltip{position:absolute;left:866px;top:38px;width:34px;height:13px;background:#111;color:#fff;font-size:8px;text-align:center;line-height:13px;border-radius:2px}
/* nav */
.nav-item{position:absolute;top:38px;width:70px;text-align:center;font-size:8px;color:var(--ink)}
.nav-item svg{display:block;margin:0 auto 6px}
.nav-item .badge{top:0}
/* panels */
.panel{position:absolute;background:var(--panel);border:1px solid var(--panel-line)}
.panel-head{height:17px;background:linear-gradient(#e6e6e6,var(--panel-head));border-bottom:1px solid var(--panel-line);font-size:9px;color:var(--ink);padding:3px 0 0 7px}
.scroll{position:absolute;right:1px;width:5px;background:#bdbdbd}
.net-row{display:flex;align-items:center;height:20px;padding-left:5px;font-size:7px;color:#555;gap:7px}
.net-mark{width:12px;height:12px;border-radius:50%;border:2px solid var(--day)}
.people-search{height:15px;border-bottom:1px solid #ccc;font-size:9px;color:#999;padding:2px 0 0 17px;position:relative}
.people-search svg{position:absolute;left:4px;top:3px}
.person{display:flex;align-items:center;height:15.6px;padding-left:4px;font-size:7px;color:#555;position:relative}
.avatar{width:12px;height:13px;background:#9a9a9a;margin-right:10px}
.online{position:absolute;right:10px;width:4px;height:4px;border-radius:50%;background:var(--online)}
/* profile */
.profile-head{position:absolute;left:370px;top:93px;width:456px;height:104px;background:linear-gradient(90deg,#1d1d1d 0%,#2a2a2a 55%,#51703a 80%,#6f9a42 100%)}
.portrait{position:absolute;left:15px;top:21px;width:62px;height:62px;background:#bdbdbd;border:2px solid #fff}
.profile-text{position:absolute;left:82px;top:16px;color:#fff;font-family:'Open Sans',Arial,sans-serif;font-size:8.5px;line-height:10.4px}
.profile-text h1{font-size:13px;font-weight:400;line-height:16px}
.tab{position:absolute;top:189px;height:16px;background:linear-gradient(#fafafa,#ddd);border:1px solid #aaa;font-size:9px;color:var(--ink);text-align:center;line-height:14px}
.tab.active{background:var(--darker);color:#fff;border-color:#111}
.cv{position:absolute;left:370px;top:213px;width:456px;height:418px;background:var(--panel);border:1px solid var(--panel-line)}
.cv h2{position:absolute;left:8px;font-size:10px;font-weight:700;color:var(--ink)}
.cv p,.cv .row{position:absolute;font-size:8px;line-height:10.4px;color:var(--text)}
.cv b{color:var(--ink)}
.cv i{font-style:italic}
.cv a{color:var(--link);text-decoration:underline}
.skills{position:absolute;left:362px;width:90px;background:var(--dark);color:#fff;font-size:8px;line-height:10.4px;padding:6px 7px}
.skills h3{font-size:8px;font-weight:700;margin-bottom:10px}
/* events */
.day{color:var(--day);font-size:8.5px;font-weight:700;padding:7px 0 0 15px}
.ev{padding:0 10px 0 15px}
.ev-title{font-size:8px;font-weight:700;color:#444;margin-top:6px;position:relative}
.ev-title .net-mark{position:absolute;left:-12px;top:0;width:9px;height:9px;border-width:2px}
.ev-text{font-size:7px;line-height:12px;color:#666;margin-top:4px}
.ev-block{background:#f7f7f7;padding-bottom:8px}
.ev-block.white{background:#fff}
/* chat */
.chat{position:absolute;top:644px;height:22px;background:#e4e4e4;border:1px solid #bcbcbc;font-size:9px;font-weight:700;color:#555;padding:5px 0 0 7px}
.chat .x{position:absolute;right:7px;top:4px;font-weight:400}
.chat .dot{display:inline-block;width:7px;height:7px;border-radius:50%;background:var(--online);margin-right:5px}
.footer{position:absolute;left:0;top:666px;width:1200px;height:27px;background:var(--footer);color:#fff;font-size:7.5px;font-weight:700}
.footer .copy{position:absolute;left:258px;top:10px}
.footer nav{position:absolute;right:257px;top:10px;display:flex;gap:9px}
</style>
</head>
<body>
<div class="world-map" role="img" aria-label="Faint outline map of the world as page backdrop"></div>

<header class="topbar">
  <div class="brand"><span class="brand-dot"></span>CIRCLE BRIGHTMOOR</div>
  <div class="search"><svg width="9" height="9" viewBox="0 0 10 10"><circle cx="4" cy="4" r="3" fill="none" stroke="#888" stroke-width="1.3"/><line x1="6.3" y1="6.3" x2="9" y2="9" stroke="#888" stroke-width="1.3"/></svg>search for people, places or networks</div>
  <div class="top-icons">
    <svg style="left:824px;top:6px" width="24" height="16" viewBox="0 0 24 16" fill="#7a7a7a"><circle cx="7" cy="5" r="3"/><circle cx="17" cy="5" r="3"/><circle cx="12" cy="4" r="3.5"/><path d="M1 15c0-5 12-5 12 0zM11 15c0-5 12-5 12 0zM5 15c0-6 14-6 14 0z"/></svg>
    <svg style="left:859px;top:7px" width="22" height="16" viewBox="0 0 22 16" fill="#7a7a7a"><rect x="1" y="1" width="13" height="9" rx="2"/><path d="M4 10l-2 4 5-4z"/><rect x="9" y="5" width="12" height="8" rx="2" fill="#999"/></svg>
    <span class="badge" style="left:860px;top:4px">5</span>
    <svg style="left:890px;top:2px" width="30" height="30" viewBox="0 0 30 30"><circle cx="15" cy="15" r="14" fill="#f4f4f4" stroke="#9a9a9a"/><circle cx="15" cy="15" r="10.5" fill="#555"/><circle cx="15" cy="12" r="3.5" fill="#fff"/><path d="M8.5 21c1-5 12-5 13 0z" fill="#fff"/></svg>
    <svg style="left:929px;top:11px" width="14" height="14" viewBox="0 0 14 14"><circle cx="7" cy="7" r="4.5" fill="none" stroke="#7a7a7a" stroke-width="3" stroke-dasharray="2.2 1.3"/><circle cx="7" cy="7" r="3.2" fill="#7a7a7a"/><circle cx="7" cy="7" r="1.5" fill="#e0e0e0"/></svg>
  </div>
</header>
<div class="tooltip">Profile</div>

<nav>
  <div class="nav-item" style="left:434px"><span class="badge" style="left:15px">10</span>
    <svg width="30" height="32" viewBox="0 0 30 32"><circle cx="6" cy="26" r="4" fill="#222"/><path d="M3 14a15 15 0 0 1 15 15M3 5a24 24 0 0 1 24 24" fill="none" stroke="#222" stroke-width="4"/></svg>News Feeds</div>
  <div class="nav-item" style="left:503px"><span class="badge" style="left:17px">5</span>
    <svg width="30" height="32" viewBox="0 0 30 32"><rect x="2" y="3" width="26" height="27" fill="#fff" stroke="#ccc"/><rect x="2" y="3" width="26" height="7" fill="#e2231a"/><text x="15" y="25" font-size="11" text-anchor="middle" fill="#222" font-family="Arimo,Arial,sans-serif">17</text></svg>Events</div>
  <div class="nav-item" style="left:564px">
    <svg width="30" height="32" viewBox="0 0 30 32" stroke="#222" stroke-width="1.2" fill="#222"><line x1="15" y1="16" x2="5" y2="5"/><line x1="15" y1="16" x2="25" y2="6"/><line x1="15" y1="16" x2="4" y2="26"/><line x1="15" y1="16" x2="26" y2="27"/><line x1="15" y1="16" x2="15" y2="3"/><circle cx="15" cy="16" r="2.5"/><circle cx="5" cy="5" r="2"/><circle cx="25" cy="6" r="2"/><circle cx="4" cy="26" r="2"/><circle cx="26" cy="27" r="2"/><circle cx="15" cy="3" r="1.6"/></svg>Networks</div>
  <div class="nav-item" style="left:627px"><span class="badge" style="left:12px">2</span>
    <svg width="38" height="32" viewBox="0 0 38 32" fill="none" stroke="#222" stroke-width="2"><rect x="3" y="6" width="14" height="11"/><rect x="21" y="6" width="14" height="11"/><path d="M10 17v4M28 17v4M4 24h30M10 24v5M28 24v5M19 21v8"/></svg>BedSwap</div>
  <div class="nav-item" style="left:695px">
    <svg width="30" height="32" viewBox="0 0 30 32"><rect x="2" y="3" width="26" height="26" rx="5" fill="#222"/><circle cx="15" cy="16" r="9" fill="#fff"/><path d="M20 11l-3 7-7 3 3-7z" fill="#222"/></svg>Expeditions</div>
</nav>

<aside class="panel" style="left:250px;top:92px;width:116px;height:93px">
  <div class="panel-head">My Networks</div>
  <div class="scroll" style="top:20px;height:30px"></div>
  <div class="net-row"><span class="net-mark"></span>Global Leaders Forum</div>
  <div class="net-row"><span class="net-mark" style="border-color:#2a6fb0"></span>Global Leaders Forum</div>
  <div class="net-row"><span class="net-mark" style="border-color:#e6d431"></span>Global Leaders Forum</div>
  <div class="net-row"><span class="net-mark" style="border-color:#8aa6d6"></span>Global Leaders Forum</div>
</aside>

<aside class="panel" style="left:250px;top:198px;width:116px;height:311px">
  <div class="people-search"><svg width="9" height="9" viewBox="0 0 10 10"><circle cx="4" cy="4" r="3" fill="none" stroke="#888" stroke-width="1.3"/><line x1="6.3" y1="6.3" x2="9" y2="9" stroke="#888" stroke-width="1.3"/></svg>search</div>
  <div class="scroll" style="top:16px;height:28px"></div>
  <div class="person"><span class="avatar" role="img" aria-label="Member photo"></span>Owen Hale<span class="online"></span></div>
  <div class="person"><span class="avatar" role="img" aria-label="Member photo"></span>Owen Hale<span class="online"></span></div>
  <div class="person"><span class="avatar" role="img" aria-label="Member photo"></span>Owen Hale<span class="online"></span></div>
  <div class="person"><span class="avatar" role="img" aria-label="Member photo"></span>Owen Hale<span class="online"></span></div>
  <div class="person"><span class="avatar" role="img" aria-label="Member photo"></span>Owen Hale<span class="online"></span></div>
  <div class="person"><span class="avatar" role="img" aria-label="Member photo"></span>Owen Hale<span class="online"></span></div>
  <div class="person"><span class="avatar" role="img" aria-label="Member photo"></span>Owen Hale<span class="online"></span></div>
  <div class="person"><span class="avatar" role="img" aria-label="Member photo"></span>Owen Hale<span class="online"></span></div>
  <div class="person"><span class="avatar" role="img" aria-label="Member photo"></span>Owen Hale<span class="online"></span></div>
  <div class="person"><span class="avatar" role="img" aria-label="Member photo"></span>Owen Hale<span class="online"></span></div>
  <div class="person"><span class="avatar" role="img" aria-label="Member photo"></span>Owen Hale<span class="online"></span></div>
</aside>

<section class="profile-head" role="img" aria-label="Profile cover: countryside road with a tree and a small house">
  <div class="portrait" role="img" aria-label="Profile portrait"></div>
  <div class="profile-text">
    <h1>Tomas Ferreira Lind</h1>
    Co-found at Circle Brightmoor and House<br>Membership:<br>Mission in life:<br>Based in:<br>Current location:
  </div>
</section>
<div class="tab active" style="left:442px;width:70px">CV</div>
<div class="tab" style="left:522px;width:71px">About Me</div>
<div class="tab" style="left:602px;width:72px">Host &amp; Travel</div>
<div class="tab" style="left:683px;width:71px">Photos</div>

<main class="cv">
  <h2 style="top:7px">Professional Summary</h2>
  <p style="left:8px;top:38px;width:340px">Lorem Ipsum is simply dummy text of the printing and typesetting industry. Lorem Ipsum has been the industry's standard dummy text ever since the 1500s, when an unknown printer took a galley of type and scrambled it to make a type specimen book.</p>
  <h2 style="top:82px">Higher Education</h2>
  <p style="left:8px;top:103px">2009 - 2012</p>
  <p style="left:87px;top:103px;width:190px"><b>Harrowgate University</b><br>Bachelor in Business Administration ( Marketing )<br>with first class<br>honours</p>
  <p style="left:288px;top:113px">Conterbury, UK</p>
  <p style="left:8px;top:154px">2008 - 2009</p>
  <p style="left:87px;top:154px;width:190px"><b>Harrowgate University</b><br>Bachelor in Business Administration ( Marketing )<br>with first class</p>
  <p style="left:304px;top:164px">Conterbury,<br>Germany</p>
  <h2 style="top:195px">Work Experience</h2>
  <p style="left:8px;top:218px">Apr 2013 - date</p>
  <p style="left:87px;top:218px;width:270px"><b>Circle Brightmoor</b>&nbsp;&nbsp;&nbsp;&nbsp;<a>View page</a><br><i>Co-founder &amp; CEO</i><br>We turn acquaintance into long lasting friendships to build a generation with more powerful networks than any generation before it.</p>
  <p style="left:8px;top:269px">Sep 2012 - Date</p>
  <p style="left:87px;top:269px"><b>Summit House</b>&nbsp;&nbsp;&nbsp;&nbsp;<a>View page</a><br>Co-founde</p>
  <h2 style="top:307px">Work Experience</h2>
  <p style="left:8px;top:330px">Apr 2013 - date</p>
  <p style="left:87px;top:330px;width:270px"><b>Circle Brightmoor</b>&nbsp;&nbsp;&nbsp;&nbsp;<a>View page</a><br><i>Co-founder &amp; CEO</i><br>We turn acquaintance into long lasting friendships to build a generation with more powerful networks than any generation before it.</p>
  <p style="left:8px;top:381px">Sep 2012 - Date</p>
  <p style="left:87px;top:381px"><b>Summit House</b>&nbsp;&nbsp;&nbsp;&nbsp;<a>View page</a><br>Co-founde</p>

  <div class="skills" style="top:9px;height:92px"><h3>Key ‘Soft’ Skills</h3>Leadership<br>Public Speaking<br>Entrepreneurship<br>Networking<br>Negotiation</div>
  <div class="skills" style="top:110px;height:93px"><h3>Key Techmocal<br>Skills</h3>Marketing<br>Java<br>C#<br>Accounting<br>Wireframing</div>
  <div class="skills" style="top:213px;height:92px"><h3>Languages</h3>English<br>German<br>Spanish<br>French<br>Norweaon</div>
</main>

<aside class="panel" style="left:830px;top:92px;width:120px;height:418px;overflow:hidden">
  <div class="panel-head">Events &amp; Deadlines</div>
  <div class="scroll" style="top:18px;height:95px"></div>
  <div class="ev-block white"><div class="day">Today</div><div class="ev"><div class="ev-title" style="margin-top:3px"><span class="net-mark"></span>Global Leaders Forum</div><div class="ev-text">Lorem Ipsum is simply dummy text of the printing and typesetting industry</div></div></div>
  <div class="ev-block"><div class="day">Tomorrow</div><div class="ev"><div class="ev-title"><span class="net-mark" style="border-color:#2a6fb0"></span>Andes Business Circle</div><div class="ev-text">Lorem Ipsum is simply dummy text of the printing and typesetting industry</div></div></div>
  <div class="ev-block white"><div class="day">Friday</div><div class="ev"><div class="ev-title"><span class="net-mark" style="border-color:#e6d431"></span>YECN</div><div class="ev-text">Lorem Ipsum is simply dummy text of the printing and typesetting industry</div><div class="ev-title" style="margin-top:9px">Ninety Consulting</div><div class="ev-text">Lorem Ipsum is simply dummy text of the printing and typesetting industry</div></div></div>
  <div class="ev-block"><div class="day">Next Week</div><div class="ev"><div class="ev-title"><span class="net-mark"></span>Andes Business Circle</div><div class="ev-text">Lorem Ipsum is simply dummy text of the printing and typesetting industry</div></div></div>
</aside>

<div class="chat" style="left:465px;width:117px">Lena Marsh<span class="x">x</span></div>
<div class="chat" style="left:587px;width:117px"><span class="dot"></span>Lena Marsh<span class="x">x</span></div>
<div class="chat" style="left:709px;width:117px"><span class="dot"></span>Lena Marsh<span class="x">x</span></div>

<footer class="footer">
  <div class="copy">CIRCLE BRIGHTMOOR © 2013</div>
  <nav><span>News Feed</span><span>Events</span><span>Networks</span><span>BedSwap</span><span>Expeditions</span></nav>
</footer>
</body>
</html>
```